Lord Bramwell's Shave & Grooming Products

Shave soap and balm label design
Lord Bramwell’s is a new brand by a business that produces gentlemen’s grooming products. Our first two products will be a shaving soap and a post shave balm. We require label designs for both. There may be additional products in the future within these categories, so it is important all text fields need to be editable. We have adopted the moose as a “mascot” and would like to incorporate that into the label in a creative way with some designer discretion. We desire the label to include a vintage/traditional/old school vibe with that will appeal to both the older and younger gentleman.
The winning designer will also have the opportunity to design future products and other designs i.e. stickers, t-shirts,
promotional material, etc. If you have any questions, feel free to ask. We look forward to seeing your designs.

Target Market(s)

Every man that shaves between the ages of 18 and 80

Industry/Entity Type

Hair And Beauty

Logo Text

Lord Bramwell's

Colors

Designer to choose colors to be used in the design.

Requirements
Must have
• SHAVE SOAP
• Our shave soap containers will be circular and need to accommodate a label sizeable from 88-100mm (exact size not finalized to date)
• SHAVE SOAP TOP LABEL REQUIREMENTS:
• TITLE Lord Bramwell’s
• SUB TITLE Fine Tallow Shave Soap
• ORIGIN Millbrook Falls, Oregon – USA
• QUANTITY Net Wt. 4.0 oz’s
• SCENT Sandalwood
• URL www.lordbramwellgoods.example
• SHAVE BALM
• Our balm container is circular and is 96mm across and 20mm tall. Label area 20mm X 300mm on the side.
• We would like a label for both the top and side of the jar. Balm label must have the following elements:
• TOP LABEL REQUIREMENTS:
• TITLE Lord Bramwell’s
• SUB TITLE Fine Post Shave Balm
• QUANTITY Net Wt. 3.0 oz’s
• SCENT Sandalwood
• SIDE LABEL REQUIREMENTS:
• TITLE Lord Bramwell’s
• ORIGIN (optional) Millbrook Falls, Oregon – USA
• SCENT Sandalwood
• INGREDIENTS Aloe Barbadensis Leaf Juice, Witch Hazel Distillate, Vitis Vinifera
• Seed Oil, Polysorbate 60, Glycerin, Vitamin E Oil, Pure Essential
• Oils, Propylene Glycol, Diazolidinyl Urea, Methylparaben, and Propylparaben
• URL (optional) www.lordbramwellgoods.example
• REQUIRED FILE FORMAT
•  Adobe Illustrator file with all vectors (not flattened)
•  all fields must be editable
Nice to have
• LOOK AND FEEL
•  Masculine
•  Bold
•  Serious
•  Traditional
•  Personable
•  Colorful
•  Value
Should not have
• Text "Fine Tallow Shave Soap" should not be more prominent than the brand name "Lord Bramwell's" See graphic below for sample.

```html
<!DOCTYPE html>
<html lang="en">
<head>
<meta charset="utf-8">
<title>Lord Bramwell’s – Fine Post Shave Balm Label</title>
<link rel="stylesheet" href="https://fonts.googleapis.com/css2?family=Alfa+Slab+One&family=Montserrat:wght@600;700&display=swap">
<style>
  :root {
    --brand-blue: #045088;
    --brand-yellow: #fde021;
    --ink: #111111;
    --paper: #eeece1;
    --paper-warm: #ebe7cf;
    --white: #ffffff;
    --canvas: #ffffff;
  }
  * { box-sizing: border-box; margin: 0; padding: 0; }
  html, body {
    width: 1200px; height: 1000px; overflow: hidden;
    background: var(--canvas);
  }
  .label {
    position: absolute; left: 261px; top: 105px;
    width: 686px; height: 780px;
    background: linear-gradient(170deg, var(--paper) 0%, var(--paper-warm) 55%, var(--paper) 100%);
  }
  .brand-band {
    position: absolute; left: 0; top: 0; width: 686px; height: 174px;
    background: var(--brand-blue);
    display: flex; align-items: center; justify-content: center;
  }
  .brand-name {
    font-family: "Montserrat", Arial, sans-serif; font-weight: 700;
    font-size: 58px; letter-spacing: 1px;
    color: var(--white); line-height: 1;
  }
  .subtitle-strip {
    position: absolute; left: 0; top: 174px; width: 686px; height: 35px;
    background: var(--white);
    font-family: "Montserrat", Arial, sans-serif; font-weight: 600;
    font-size: 23px; letter-spacing: 12.4px; color: var(--ink);
    text-align: center; line-height: 36px; padding-left: 12px;
  }
  .accent-rule {
    position: absolute; left: 0; top: 209px; width: 686px; height: 8px;
    background: var(--brand-yellow);
  }
  .scent-name {
    position: absolute; left: 0; top: 452px; width: 686px; text-align: center;
    font-family: "Alfa Slab One", Georgia, serif; font-size: 40px;
    letter-spacing: 15px; padding-left: 15px; color: var(--white);
    -webkit-text-stroke: 1.5px var(--ink);
    text-shadow: 2px 2px 0 var(--ink), 3px 3px 0 var(--ink), 4px 4px 0 var(--ink);
  }
  .product-type {
    position: absolute; left: 0; top: 510px; width: 686px; text-align: center;
    font-family: "Montserrat", Arial, sans-serif; font-weight: 700;
    font-size: 28px; letter-spacing: 5px; color: var(--ink);
  }
  .label-footer {
    position: absolute; left: 0; top: 746px; width: 686px; text-align: center;
    font-family: "Montserrat", Arial, sans-serif; font-weight: 700;
    font-size: 10.5px; letter-spacing: 0.5px; color: var(--ink);
  }
  .label-footer .divider { margin: 0 6px; }
</style>
</head>
<body>
  <div class="label">
    <header class="brand-band">
      <h1 class="brand-name">Lord Bramwell’s</h1>
    </header>
    <div class="subtitle-strip">FINE POST SHAVE BALM</div>
    <div class="accent-rule"></div>

    <p class="scent-name">SANDALWOOD</p>
    <p class="product-type">SHAVE BALM</p>

    <footer class="label-footer">
      MILLBROOK FALLS, OREGON – USA<span class="divider">|</span>URL WWW.LORDBRAMWELLGOODS.EXAMPLE<span class="divider">|</span>NET WT. 3.0 OZ
    </footer>
  </div>
</body>
</html>
```